Re-branding for Structural Engineering firm

We need new business cards as part of our current re-branding. We have a new logo (attached), so the card design should incorporate this color scheme. We are a structural engineering firm providing structural building design and seismic consulting services. The final design should communicate professionalism and stability, with a modern look and feel.

```html
<!DOCTYPE html>
<html lang="en">
<head>
<meta charset="utf-8">
<title>Northline Structural – Business Card</title>
<link rel="stylesheet" href="https://fonts.googleapis.com/css2?family=Arimo:wght@400&family=Lato:wght@400;700&display=swap">
<style>
  :root {
    --stage: #201c1a;
    --card: #ececec;
    --brand-blue: #2e64a9;
    --brand-gray: #717171;
    --text-gray: #6a6a6a;
    --white: #ffffff;
  }
  html, body {
    margin: 0;
    width: 1200px;
    height: 1200px;
    overflow: hidden;
    background: var(--stage);
  }
  .card {
    position: absolute;
    left: 100px;
    top: 306px;
    width: 1000px;
    height: 587px;
    background: var(--card);
    overflow: hidden;
    font-family: "Arimo", Arial, sans-serif;
  }
  .corner-shapes {
    position: absolute;
    inset: 0;
  }
  .holder {
    position: absolute;
    left: 65px;
    top: 64px;
  }
  .holder-name {
    margin: 0;
    font-size: 33px;
    font-weight: 400;
    color: var(--brand-blue);
    line-height: 1.1;
  }
  .holder-title {
    margin: 0;
    font-size: 29px;
    color: var(--text-gray);
    line-height: 1.1;
  }
  .brand {
    position: absolute;
    left: 435px;
    top: 67px;
    display: flex;
    align-items: stretch;
  }
  .brand-square {
    width: 170px;
    height: 172px;
    background: var(--brand-blue);
  }
  .brand-divider {
    width: 2px;
    background: var(--brand-gray);
    margin: 0 21px 0 12px;
  }
  .brand-text {
    font-family: "Lato", sans-serif;
    display: flex;
    flex-direction: column;
  }
  .brand-name {
    margin: -4px 0 0;
    font-size: 46px;
    font-weight: 700;
    line-height: 0.95;
    color: var(--brand-blue);
    letter-spacing: 0.5px;
  }
  .brand-address {
    margin: 12px 0 0;
    font-size: 20px;
    line-height: 27px;
    color: var(--text-gray);
    font-style: normal;
  }
  .brand-address .sep {
    color: var(--brand-blue);
    padding: 0 6px;
  }
  .contact-row {
    position: absolute;
    left: 0;
    right: 0;
    top: 524px;
    display: flex;
    justify-content: center;
    gap: 38px;
    font-size: 25px;
    color: var(--text-gray);
  }
  .contact-item {
    display: flex;
    align-items: center;
    gap: 8px;
  }
  .contact-item svg {
    width: 24px;
    height: 24px;
    fill: var(--brand-blue);
  }
</style>
</head>
<body>
  <section class="card">
    <svg class="corner-shapes" width="1000" height="587" viewBox="0 0 1000 587">
      <polygon points="0,300 146,300 146,435 11,587 0,587" fill="var(--brand-gray)"/>
      <line x1="84" y1="398" x2="104" y2="422" stroke="var(--white)" stroke-width="9"/>
      <polygon points="854,300 1000,300 1000,587 989,587 854,435" fill="var(--brand-blue)"/>
      <line x1="916" y1="398" x2="896" y2="422" stroke="var(--white)" stroke-width="9"/>
    </svg>

    <header class="holder">
      <h1 class="holder-name">Reid Halvorsen, S.E.</h1>
      <p class="holder-title">Principal</p>
    </header>

    <div class="brand">
      <div class="brand-square"></div>
      <div class="brand-divider"></div>
      <div class="brand-text">
        <p class="brand-name">NORTHLINE<br>STRUCTURAL</p>
        <address class="brand-address">
          4410 Harbor Crest Dr., Ste. 210<br>
          Bayview, California 90000<br>
          555.201.4400<span class="sep">|</span>www.northlinese.com
        </address>
      </div>
    </div>

    <div class="contact-row">
      <span class="contact-item">
        <svg viewBox="0 0 24 24" aria-hidden="true"><path d="M3 9c3-4 15-4 18 0l-3 2-2-2H8L6 11zM5 12h14l1 9H4z"/></svg>
        555.201.4402
      </span>
      <span class="contact-item">
        <svg viewBox="0 0 24 24" aria-hidden="true"><path d="M7 1h10a1 1 0 0 1 1 1v20a1 1 0 0 1-1 1H7a1 1 0 0 1-1-1V2a1 1 0 0 1 1-1zm1 3v15h8V4z"/></svg>
        555.318.7720
      </span>
      <span class="contact-item">
        <svg viewBox="0 0 24 24" aria-hidden="true"><path d="M2 9l10-7 10 7v12H2zm2 2v8h16v-8l-8 5z"/></svg>
        reid@northlinese.com
      </span>
    </div>
  </section>
</body>
</html>
```